Aldercrest Chiropractic Rehabilitation and Wellness
Business Card, Portfolio Folder, Stationary, Postcard
Simple
Marlow Tenney
Doctor of Chiropractic
518 Verbena Ridge Avenue
Chico, CA 95926
marlow@alderbrook.com
www.alderbrook.com
Fonts are TrajanPro and Corbel
Logo and URL or just logo
Logo
jpg Logo

```html
<!DOCTYPE html>
<html lang="en">
<head>
<meta charset="utf-8">
<title>Aldercrest Chiropractic Stationery</title>
<link href="https://fonts.googleapis.com/css2?family=Cinzel:wght@600&family=Source+Sans+3:wght@400;600&display=swap" rel="stylesheet">
<style>
  :root {
    --backdrop: #a8a8a8;
    --paper: #ffffff;
    --blue-deep: #15599f;
    --blue-mid: #2a7fc8;
    --blue-light: #5fb2e6;
    --green: #8cc63f;
    --ink: #1c4f86;
    --grey-text: #555b61;
    --fold: #c9cdd1;
  }
  * { margin: 0; padding: 0; box-sizing: border-box; }
  html, body { width: 1200px; height: 684px; overflow: hidden; }
  body { background: var(--backdrop); position: relative; font-family: "Source Sans 3", Arial, sans-serif; }

  .sheet { position: absolute; background: var(--paper); box-shadow: 0 2px 6px rgba(0,0,0,.25); overflow: hidden; }
  .band-top { position: absolute; left: 0; right: 0; top: 0; background: linear-gradient(90deg, var(--blue-deep), var(--blue-light) 50%, var(--blue-deep)); border-bottom: 3px solid var(--green); }
  .band-bottom { position: absolute; left: 0; right: 0; bottom: 0; background: linear-gradient(90deg, var(--blue-deep), var(--blue-light) 50%, var(--blue-deep)); border-top: 3px solid var(--green); display: flex; align-items: center; justify-content: center; color: #fff; font-size: 8px; letter-spacing: .3px; }

  .brand { position: absolute; display: flex; align-items: center; gap: 5px; white-space: nowrap; }
  .brand-dot { border-radius: 50%; background: var(--blue-mid); flex: none; }
  .brand-text { display: flex; flex-direction: column; }
  .brand-name { font-family: "Cinzel", serif; font-weight: 600; color: var(--ink); line-height: 1; letter-spacing: .5px; }
  .brand-tag { font-family: "Source Sans 3", Arial, sans-serif; color: var(--ink); line-height: 1.2; }

  .contact-line { position: absolute; left: 0; right: 0; text-align: center; font-size: 6px; color: var(--grey-text); white-space: nowrap; }

  /* letterhead */
  .letterhead { left: 322px; top: 12px; width: 316px; height: 665px; }
  .letterhead .band-top { height: 18px; }
  .letterhead .band-bottom { height: 34px; }
  .letterhead .brand { left: 50%; top: 60px; transform: translateX(-50%); }
  .letterhead .brand-dot { width: 32px; height: 32px; }
  .letterhead .brand-name { font-size: 14px; }
  .letterhead .brand-tag { font-size: 5px; }
  .letterhead .contact-line { bottom: 44px; font-size: 5.5px; }

  /* envelope back */
  .envelope-back { left: 648px; top: 91px; width: 530px; height: 264px; }
  .envelope-back svg { position: absolute; inset: 0; }
  .envelope-back .brand-dot { position: absolute; left: 248px; top: 36px; width: 34px; height: 34px; }

  /* envelope front (postcard) */
  .envelope-front { left: 648px; top: 377px; width: 530px; height: 230px; }
  .envelope-front .band-top { height: 16px; }
  .envelope-front .band-bottom { height: 26px; font-size: 7px; }
  .envelope-front .brand { left: 50%; top: 32px; transform: translateX(-50%); }
  .envelope-front .brand-dot { width: 32px; height: 32px; }
  .envelope-front .brand-name { font-size: 14px; }
  .envelope-front .brand-tag { font-size: 5px; }
  .envelope-front .contact-line { bottom: 34px; }

  /* business cards */
  .card { width: 200px; left: 31px; }
  .card-back { top: 221px; height: 103px; }
  .card-back .band-top { height: 18px; }
  .card-back .band-bottom { height: 18px; }
  .card-back .brand-dot { position: absolute; left: 84px; top: 35px; width: 32px; height: 32px; }

  .card-front { top: 348px; height: 144px; }
  .card-front .band-top { height: 12px; }
  .card-front .band-bottom { height: 16px; font-size: 6px; }
  .card-front .brand { left: 10px; top: 22px; gap: 4px; }
  .card-front .brand-dot { width: 18px; height: 18px; }
  .card-front .brand-name { font-size: 10px; }
  .card-front .brand-tag { font-size: 4.5px; }
  .card-person { position: absolute; left: 12px; top: 56px; color: var(--grey-text); font-size: 5px; line-height: 1.35; }
  .card-person .person-name { font-size: 6.5px; font-weight: 600; color: var(--ink); }
  .card-person .gap { height: 5px; }
</style>
</head>
<body>

  <section class="sheet letterhead">
    <div class="band-top"></div>
    <div class="brand">
      <span class="brand-dot"></span>
      <span class="brand-text">
        <span class="brand-name">Aldercrest</span>
        <span class="brand-tag">Chiropractic Rehabilitation and Wellness</span>
      </span>
    </div>
    <p class="contact-line">P (530) 555-0142 | E marlow@alderbrook.com | A 518 Verbena Ridge Avenue Chico, CA 95926</p>
    <div class="band-bottom">www.alderbrook.com</div>
  </section>

  <section class="sheet envelope-back">
    <svg width="530" height="264" viewBox="0 0 530 264">
      <path d="M1 1 L228 105 Q265 124 302 105 L529 1" fill="none" stroke="var(--fold)" stroke-width="1.2"/>
      <path d="M1 263 L200 150 M529 263 L330 150" fill="none" stroke="var(--fold)" stroke-width="1"/>
    </svg>
    <span class="brand-dot"></span>
  </section>

  <section class="sheet envelope-front">
    <div class="band-top"></div>
    <div class="brand">
      <span class="brand-dot"></span>
      <span class="brand-text">
        <span class="brand-name">Aldercrest</span>
        <span class="brand-tag">Chiropractic Rehabilitation and Wellness</span>
      </span>
    </div>
    <p class="contact-line">P (530) 555-0142 | E marlow@alderbrook.com | A 518 Verbena Ridge Avenue Chico, CA 95926</p>
    <div class="band-bottom">www.alderbrook.com</div>
  </section>

  <section class="sheet card card-back">
    <div class="band-top"></div>
    <span class="brand-dot"></span>
    <div class="band-bottom"></div>
  </section>

  <section class="sheet card card-front">
    <div class="band-top"></div>
    <div class="brand">
      <span class="brand-dot"></span>
      <span class="brand-text">
        <span class="brand-name">Aldercrest</span>
        <span class="brand-tag">Chiropractic Rehabilitation and Wellness</span>
      </span>
    </div>
    <div class="card-person">
      <div class="person-name">Marlow Tenney</div>
      <div>Doctor of Chiropractic</div>
      <div class="gap"></div>
      <div>(530) 555-0142</div>
      <div>marlow@alderbrook.com</div>
      <div>518 Verbena Ridge Avenue</div>
      <div>Chico, CA 95926</div>
    </div>
    <div class="band-bottom">www.alderbrook.com</div>
  </section>

</body>
</html>
```